Conference website: Kestrel Meridian Forum 2015

We need a web design to help develop a modern and interactive website for the 2nd Kestrel Meridian Summit which main objective will be to present and discuss real-life KmR business initiatives being implemented by entrepreneurs and corporate innovators that are driving sustainable innovation from the bottom up

This is a bi-annual event and will build on the 1st Kestrel Meridian Forum
http://www.kestrelmeridian.org/summit-2013. It is important that the new website maintain consistency with the 1) the Kestrel Meridian Logo (www.kestrelmeridian.org), 2) the visual identity from the fist event and 3) the organization TLQ Logo (www.t7lq.org) -- but the design should be modern, clean, and crisp.

Target Market(s)

Corporations, academics, executives, entrepreneurs, consultants, multilateral organizations, founders, institutions

Industry/Entity Type

Business

Coding

Coded - Design and coding required

Number of Pages Required

5+ page

Font styles to use
Sans Serif

Colors
f68d4d
9bcb3b
3276b5
faa54b
00a88f
0792cd
f37022
9bcb3c
0355a3

Requirements
Must have
• maintain consistency with Kestrel Meridian Logo
• dynamic to get the attention
• design modern, clean and crisp
• content should be well linked (e.i. photos and bios liked to the name of speaker on sessions).
• Has to link to a registration system
• Needs to be under the Kestrel Meridian domain www.kestrelmeridian.org
• Preference to URL kestrelmeridian.org/Summit2015
Nice to have
• different techniques to display menus, photos and bios and description of sessions
• connect somehow with the visual communication developed on last summit in 2013
Should not have
• should not be the same previously
• should not be traditional
• should not be static

```html
<!DOCTYPE html>
<html lang="en">
<head>
<meta charset="utf-8">
<title>Kestrel Meridian Forum 2015</title>
<link href="https://fonts.googleapis.com/css2?family=Mulish:wght@400;600;700&family=Open+Sans:wght@400;600;700&display=swap" rel="stylesheet">
<style>
:root{
  --green:#1d8a3f;
  --green-head:#1f8a3a;
  --blue:#0a62c2;
  --blue-deep:#0a4fa6;
  --ink:#3b3b3b;
  --muted:#6a6a6a;
  --rule:#dcdcdc;
  --grey-band:#e6e7e9;
  --footer:#3a3a3a;
  --footer-text:#d8d8d8;
  --white:#ffffff;
}
*{box-sizing:border-box;margin:0;padding:0}
html,body{width:1200px;height:2540px;overflow:hidden;background:var(--white)}
body{font-family:"Open Sans",Arial,sans-serif;color:var(--ink);position:relative}
.head-font{font-family:"Mulish","Open Sans",sans-serif}

.topbar{position:absolute;top:0;left:0;width:1200px;height:28px;background:var(--green);color:var(--white);font-size:12px;font-weight:600}
.topbar .phone{position:absolute;left:75px;top:6px}
.topbar .social{position:absolute;right:75px;top:5px;display:flex;gap:6px}
.topbar .social span{width:18px;height:18px;border-radius:50%;background:var(--white);display:block}

.masthead{position:absolute;top:28px;left:0;width:1200px;height:137px;background:#f4f5f5}
.brand{position:absolute;left:75px;top:22px;display:flex;align-items:center;gap:12px}
.brand .mark{width:86px;height:86px;background:var(--blue-deep)}
.brand .name{font-family:"Mulish",sans-serif;font-weight:700;font-size:26px;color:var(--blue-deep);line-height:1.05}
.summit-title{position:absolute;left:418px;top:42px;font-family:"Mulish",sans-serif;font-weight:600;font-size:24px;color:var(--green-head);letter-spacing:1px}
.mainnav{position:absolute;left:418px;top:92px;display:flex;gap:22px;font-family:"Mulish",sans-serif;font-weight:700;font-size:14px;color:var(--green-head);letter-spacing:.3px}
.partners{position:absolute;left:728px;top:30px;display:flex;gap:26px;align-items:center}
.partner{display:flex;align-items:center;gap:8px;font-family:"Mulish",sans-serif;font-weight:700;font-size:15px;color:var(--ink)}
.partner i{width:30px;height:30px;border-radius:50%;background:#9aa5ae;display:block}
.lang{position:absolute;left:1030px;top:34px;display:flex;gap:14px}
.lang span{width:38px;height:24px;display:block;border-radius:3px}
.lang .en{background:var(--green)}
.lang .pt{background:#2a9a45;width:32px}

.hero{position:absolute;top:165px;left:0;width:1015px;height:353px;background:linear-gradient(160deg,#c7ced6 0%,#aeb6bd 45%,#6d5a55 100%)}
.hero .prev{position:absolute;left:75px;top:158px;width:54px;height:54px;background:rgba(90,90,90,.75)}
.sidemenu{position:absolute;top:165px;left:1015px;width:185px;height:353px;background:var(--white);list-style:none}
.sidemenu li{height:44px;line-height:44px;padding-left:18px;font-size:12px;border-bottom:1px solid var(--rule);color:var(--ink)}
.sidemenu li.active{background:var(--green);color:var(--white);font-weight:600}

.titleband{position:absolute;top:518px;left:0;width:1200px;height:102px;background:var(--blue);color:var(--white);text-align:center}
.titleband h1{font-family:"Mulish",sans-serif;font-weight:600;font-size:25px;line-height:102px}

.intro{position:absolute;top:620px;left:0;width:1200px;height:180px;background:var(--grey-band);padding:38px 75px 0;font-size:11px;line-height:21px;color:var(--muted)}
.intro p{margin-bottom:12px;max-width:1050px}
.intro a{color:var(--blue);font-weight:600;text-decoration:none}

.announce{position:absolute;top:840px;left:75px;width:235px}
.announce h2{font-family:"Mulish",sans-serif;font-weight:400;font-size:26px;color:var(--ink);margin-bottom:16px}
.announce ul{list-style:none;border-left:1px solid var(--rule)}
.announce li{padding:10px 12px;border-bottom:1px solid var(--rule);font-size:11.5px;font-weight:700;line-height:16px;color:var(--ink)}
.announce li small{display:block;font-size:10px;font-weight:400;color:var(--muted);margin-top:3px}
.announce li.current{background:var(--blue);color:var(--white)}
.announce li.current small{color:#dbe7f6}
.announce .more{display:block;text-align:right;margin-top:16px;font-size:12px;font-weight:600;color:var(--blue-deep)}

.content{position:absolute;top:840px;left:352px;width:778px}
.content h2{font-family:"Mulish",sans-serif;font-weight:600;font-size:32px;color:var(--green-head);margin-bottom:28px}
.content p{font-size:11px;line-height:21px;color:var(--muted);margin-bottom:16px}
.content section{margin-bottom:36px}

.speakers{position:absolute;top:1470px;left:352px;width:778px;height:300px}
.speakers .arrow{position:absolute;top:80px}
.speakers .arrow.left{left:0}.speakers .arrow.right{right:0}
.speaker{position:absolute;top:0;width:180px;text-align:center}
.speaker .photo{width:170px;height:170px;border-radius:50%;margin:0 auto;background:linear-gradient(180deg,#d9cfc6,#8a7566);border:3px solid #e7e7e7}
.speaker h3{font-family:"Mulish",sans-serif;font-weight:600;font-size:20px;margin-top:24px;color:var(--ink)}
.speaker p{font-size:11px;line-height:18px;color:var(--muted);margin-top:4px}
.speaker .btn{display:inline-block;margin-top:10px;background:var(--blue);color:var(--white);font-size:10px;padding:3px 16px}

.mission{position:absolute;top:1810px;left:0;width:1200px;height:420px;background:linear-gradient(110deg,#10499a 0%,#0f5ec4 55%,#0a66d4 100%)}
.mission .copy{position:absolute;left:640px;top:60px;width:490px;color:var(--white)}
.mission h2{font-family:"Mulish",sans-serif;font-weight:400;font-size:40px;line-height:48px}
.mission h2 span{display:block;font-size:31px}
.mission p{font-size:11.5px;line-height:22px;margin-top:40px;font-weight:600}
.mission .cta{display:inline-block;margin-top:28px;border:2px solid var(--white);width:198px;height:40px;line-height:36px;text-align:center;font-size:13px}

.footer{position:absolute;top:2230px;left:0;width:1200px;height:255px;background:var(--footer);color:var(--footer-text)}
.footer .col{position:absolute;top:48px}
.footer h4{font-family:"Mulish",sans-serif;font-weight:400;font-size:21px;color:var(--white);margin-bottom:20px}
.footer p{font-size:11px;line-height:19px;margin-bottom:14px}
.footer .social{display:flex;gap:6px}
.footer .social span{width:18px;height:18px;border-radius:50%;background:var(--white);display:block}

.copyright{position:absolute;top:2485px;left:0;width:1200px;height:55px;background:#f2f2f2;text-align:center;line-height:55px;font-size:11px;color:var(--ink)}
</style>
</head>
<body>

<div class="topbar">
  <span class="phone">Phone: (555) 214-0386</span>
  <div class="social"><span></span><span></span><span></span><span></span><span></span></div>
</div>

<header class="masthead">
  <div class="brand"><div class="mark"></div><div class="name">Kestrel<br>Meridian</div></div>
  <div class="summit-title">SUMMIT 2015</div>
  <nav class="mainnav"><span>KESTREL MERIDIAN</span><span>KNOWLEDGE BASE</span><span>SPONSORS &amp; PARTNERS</span><span>JOIN US</span><span>EVENTS</span><span>CONTACT US</span></nav>
  <div class="partners">
    <div class="partner"><i></i>Lumen Institute</div>
    <div class="partner"><i></i>TLQ</div>
  </div>
  <div class="lang"><span class="en"></span><span class="pt"></span></div>
</header>

<div class="hero" role="img" aria-label="Photo of a smiling woman carrying a child on her back, with another woman beside her, in the highlands">
  <div class="prev"><svg width="54" height="54" viewBox="0 0 54 54"><path d="M31 16 L20 27 L31 38" fill="none" stroke="#fff" stroke-width="4"/></svg></div>
</div>
<ul class="sidemenu">
  <li class="active">About the Summit</li>
  <li>Sponsors &amp; Partners</li>
  <li>Registration</li>
  <li>Program</li>
  <li>Logistic</li>
  <li>Organizers</li>
  <li>Contact</li>
  <li>Application Forms</li>
</ul>

<div class="titleband"><h1>Lifting the Poor Through Business: First International Kestrel Meridian Forum</h1></div>

<div class="intro">
  <p>New business models and products, innovation ecosystems, sustainability, financial education, and how to bring new opportunities to the world's poorest populations were among the main topics of the first international Kestrel Meridian Forum.</p>
  <p>The event mobilized corporate leaders, non-profits, KmR Lab leaders, students, academics, entrepreneurs, community and government representatives, and journalists, on 7 and 8 November, 2013, at the headquarters of Verdance, in Cajamar, São Paulo... <a href="#">Read More</a></p>
</div>

<aside class="announce">
  <h2>Announcements</h2>
  <ul>
    <li class="current">FUNDER BRIEFING Kogi Sacred Sites of the Sierra Nevada de Santa Marta, Colombia Monday June 2 9am to 11am<small>June 1, 2014</small></li>
    <li>Registration for 2014 World Summit on Indigenous Philanthropy now open<small>May 22, 2014</small></li>
    <li>KmR is offering exciting internships this summer!<small>May 15, 2014</small></li>
    <li>Interview with Dana Holloway<small>April 22, 2014</small></li>
    <li>2015 KmR Summit Call for Sessions<small>April 20, 2014</small></li>
    <li>Funders Briefing – Panel Discussion honoring 2014 Alderwood Environmental Prize Winner from South America<small>April 15, 2014</small></li>
    <li>Marisol Teague on Indigenous Philanthropy (Heritage Voices)<small>April 14, 2014</small></li>
  </ul>
  <span class="more">View More</span>
</aside>

<main class="content">
  <section>
    <h2>About the Summit</h2>
    <p>There are many variations of passages of Lorem Ipsum available, but the majority have suffered alteration in some form, by injected humour, or randomised words which don't look even slightly believable. If you are going to use a passage of Lorem Ipsum, you need to be sure there isn't anything embarrassing hidden in the middle of text.</p>
    <p>All the Lorem Ipsum generators on the Internet tend to repeat predefined chunks as necessary, making this the first true generator on the Internet. It uses a dictionary of over 200 Latin words, combined with a handful of model sentence structures, to generate Lorem Ipsum which looks reasonable. The generated Lorem Ipsum is therefore always free from repetition, injected humour, or non-characteristic words etc.</p>
  </section>
  <section>
    <h2>History</h2>
    <p>There are many variations of passages of Lorem Ipsum available, but the majority have suffered alteration in some form, by injected humour, or randomised words which don't look even slightly believable. If you are going to use a passage of Lorem Ipsum, you need to be sure there isn't anything embarrassing hidden in the middle of text.</p>
    <p>All the Lorem Ipsum generators on the Internet tend to repeat predefined chunks as necessary, making this the first true generator on the Internet. It uses a dictionary of over 200 Latin words, combined with a handful of model sentence structures, to generate Lorem Ipsum which looks reasonable. The generated Lorem Ipsum is therefore always free from repetition, injected humour, or non-characteristic words etc.</p>
  </section>
  <h2>Speakers</h2>
</main>

<div class="speakers">
  <svg class="arrow left" width="20" height="30" viewBox="0 0 20 30"><path d="M15 3 L4 15 L15 27" fill="none" stroke="#9a9a9a" stroke-width="2"/></svg>
  <svg class="arrow right" width="20" height="30" viewBox="0 0 20 30"><path d="M5 3 L16 15 L5 27" fill="none" stroke="#9a9a9a" stroke-width="2"/></svg>
  <div class="speaker" style="left:70px"><div class="photo" role="img" aria-label="Portrait photo of a speaker"></div><h3>Loram Ipsum</h3><p>Lorem Ipsum is simply dummy text of the printing and typesetting</p><span class="btn">Read More</span></div>
  <div class="speaker" style="left:275px"><div class="photo" role="img" aria-label="Portrait photo of a speaker"></div><h3>Loram Ipsum</h3><p>Lorem Ipsum is simply dummy text of the printing and typesetting</p><span class="btn">Read More</span></div>
  <div class="speaker" style="left:480px"><div class="photo" role="img" aria-label="Portrait photo of a speaker"></div><h3>Loram Ipsum</h3><p>Lorem Ipsum is simply dummy text of the printing and typesetting</p><span class="btn">Read More</span></div>
</div>

<section class="mission" role="img" aria-label="Blue-tinted photo of children praying together">
  <div class="copy">
    <h2>Raising the base of<span>the pyramid through enterprise</span></h2>
    <p>Lorem Ipsum is simply dummy text of the printing and typesetting industry. Lorem Ipsum has been the industry's standard dummy text ever since the 1500s, when an unknown printer took a galley of type and scrambled it to make a type specimen book.</p>
    <span class="cta">View More</span>
  </div>
</section>

<footer class="footer">
  <div class="col" style="left:75px;width:340px">
    <h4>About Us</h4>
    <p>There are many variations of passages of Lorem Ipsum available, but the majority have suffered alteration in some form, by injected humour, or randomised words which don't look even slightly believable. If you are going to use a passage of Lorem Ipsum, you need to be sure there isn't anything embarrassing hidden in the middle of text.</p>
  </div>
  <div class="col" style="left:540px;width:260px">
    <h4>Contact Us</h4>
    <p>42 Larkspur Lane,<br>Fernvale, OR 97001 USA</p>
    <p>(555) 214-0386</p>
    <div class="social"><span></span><span></span><span></span><span></span><span></span></div>
  </div>
  <div class="col" style="left:882px;width:245px">
    <h4>Latest News</h4>
    <p>There are many variations of passages of Lorem Ipsum available, but the majority</p>
    <p>There are many variations of passages of Lorem Ipsum available, but the majority</p>
  </div>
</footer>

<div class="copyright">© Copyright 2012-2014 by kestrelmeridian.org. All rights reserved.</div>

</body>
</html>
```